Young Pilgrims-2017

a Spiritual journey for the years to follow

Package Includes :
- Under Guidance of a Sheikh
- 5 Star Accommodation in Medina & Makkah
- 4 - 5 Person Sharing
- 20 - 22 Days Trip
- Post and Pre Lectures
- Age Group 18+ Years
- For Brothers & Families

With Rehan Jameel Farooqui
& Brother Bilal Qureshi

Contact :
Bilal Qureshi +92 333 5810462
bilalqureshi@[url removed, login to view]

```html
<!DOCTYPE html>
<html lang="en">
<head>
<meta charset="utf-8">
<title>Young Pilgrims 2017</title>
<link href="https://fonts.googleapis.com/css2?family=Lora:ital,wght@0,600;0,700;1,600;1,700&family=Open+Sans:wght@400;600;700&display=swap" rel="stylesheet">
<style>
  :root {
    --stage: #ebe6dd;
    --paper: #f3f0ea;
    --paper-shade: #e2ddd3;
    --brown-dark: #3b2a1a;
    --brown: #5a4128;
    --brown-text: #4a3116;
    --gold: #f2c200;
    --gold-deep: #c99a12;
    --ink: #2e2a26;
    --white: #ffffff;
  }
  * { margin: 0; padding: 0; box-sizing: border-box; }
  html, body { width: 1200px; height: 745px; overflow: hidden; }
  body { background: var(--stage); position: relative; }

  .poster {
    position: absolute; left: 350px; top: 20px;
    width: 500px; height: 706px; overflow: hidden;
    background: radial-gradient(ellipse at 50% 40%, var(--paper) 0%, var(--paper) 45%, var(--paper-shade) 100%);
    box-shadow: 0 6px 18px rgba(0,0,0,.25);
  }

  .title-band {
    position: absolute; left: 0; top: 37px; width: 100%; height: 60px;
    background: linear-gradient(90deg, rgba(90,65,40,.15) 0%, var(--brown) 22%, var(--brown) 78%, rgba(90,65,40,.15) 100%);
    border-top: 2px solid var(--gold-deep); border-bottom: 2px solid var(--gold-deep);
  }
  .title {
    position: absolute; left: 0; top: 41px; width: 100%;
    text-align: center; font-family: "Lora", serif; font-weight: 700;
    font-size: 40px; line-height: 52px; color: var(--white);
  }
  .lantern {
    position: absolute; top: 44px; width: 20px; height: 46px;
    background: linear-gradient(180deg, var(--gold) 0%, var(--gold-deep) 100%);
    border-radius: 10px 10px 4px 4px; opacity: .85;
  }
  .lantern.left { left: 28px; }
  .lantern.right { right: 28px; }

  .tagline {
    position: absolute; left: 0; top: 112px; width: 100%;
    text-align: center; font-family: "Lora", serif; font-weight: 600;
    font-size: 20px; color: var(--brown-text);
  }
  .flourish {
    position: absolute; left: 195px; top: 146px; width: 110px; height: 26px;
    background: linear-gradient(90deg, transparent, rgba(74,49,22,.55), transparent);
    border-radius: 13px;
  }

  .divider { position: absolute; left: 0; width: 100%; }
  .divider.top { top: 188px; height: 36px; }
  .divider.bottom { top: 355px; height: 8px; }

  .package-heading {
    position: absolute; left: 0; top: 222px; width: 100%;
    text-align: center; font-family: "Lora", serif; font-style: italic; font-weight: 700;
    font-size: 14px; color: var(--gold-deep);
  }

  .feature {
    position: absolute; font-family: "Open Sans", sans-serif; font-weight: 600;
    font-size: 12px; line-height: 15px; color: var(--ink);
    padding-left: 24px;
  }
  .feature::before {
    content: ""; position: absolute; left: 0; top: -1px;
    width: 16px; height: 16px; border-radius: 50%;
    background: radial-gradient(circle, var(--gold) 0 3px, var(--white) 3.5px);
    box-shadow: 0 0 0 1.5px var(--paper-shade), 0 1px 2px rgba(0,0,0,.3);
  }

  .scene {
    position: absolute; left: 40px; top: 392px; width: 420px; height: 245px;
    background: linear-gradient(180deg, #ffffff 0%, #ecebe8 55%, #8a7a52 100%);
    border-radius: 6px 6px 0 0; opacity: .9;
  }

  .with {
    position: absolute; left: 0; top: 422px; width: 100%;
    text-align: center; font-family: "Lora", serif; font-style: italic; font-weight: 600;
    font-size: 18px; color: var(--brown-text);
  }
  .guides {
    position: absolute; left: 0; top: 446px; width: 100%;
    text-align: center; font-family: "Open Sans", sans-serif; font-weight: 700;
    font-size: 12.5px; line-height: 22px; color: var(--brown-text);
  }

  .footer-band { position: absolute; left: 0; top: 600px; width: 100%; height: 106px; }

  .contact-name {
    position: absolute; left: 0; top: 644px; width: 100%;
    text-align: center; font-family: "Open Sans", sans-serif; font-weight: 600;
    font-size: 13px; color: var(--white);
  }
  .contact-row {
    position: absolute; top: 669px; display: flex; align-items: center; gap: 7px;
    font-family: "Open Sans", sans-serif; font-weight: 600; font-size: 11px; color: var(--white);
  }
  .contact-row.phone { left: 24px; }
  .contact-row.email { left: 168px; }
  .contact-row.web { left: 350px; }
  .contact-icon { width: 18px; height: 18px; flex: none; }
</style>
</head>
<body>
  <main class="poster">
    <div class="title-band"></div>
    <div class="lantern left" role="img" aria-label="Hanging lantern ornament"></div>
    <div class="lantern right" role="img" aria-label="Hanging lantern ornament"></div>
    <h1 class="title">Young Pilgrims 2017</h1>

    <p class="tagline">A Spiritual journey for the years to follow</p>
    <div class="flourish" role="img" aria-label="Decorative flourish ornament"></div>

    <svg class="divider top" viewBox="0 0 500 36" preserveAspectRatio="none" aria-hidden="true">
      <defs>
        <linearGradient id="goldFade" x1="0" x2="1">
          <stop offset="0" stop-color="#c99a12" stop-opacity="0"/>
          <stop offset=".2" stop-color="#f2c200"/>
          <stop offset=".8" stop-color="#f2c200"/>
          <stop offset="1" stop-color="#c99a12" stop-opacity="0"/>
        </linearGradient>
      </defs>
      <path d="M0 30 L200 30 Q235 30 250 4 Q265 30 300 30 L500 30" fill="none" stroke="url(#goldFade)" stroke-width="3"/>
    </svg>
    <p class="package-heading">Package Includes</p>

    <p class="feature" style="left:72px; top:259px;">Under Guidance of a Sheikh</p>
    <p class="feature" style="left:72px; top:284px;">5 Star Accommodation in<br>Medina &amp; Makkah</p>
    <p class="feature" style="left:72px; top:321px;">4 – 5 Person Sharing</p>
    <p class="feature" style="left:295px; top:259px;">Post and Pre Lectures</p>
    <p class="feature" style="left:295px; top:284px;">Age Group 18+ Years</p>
    <p class="feature" style="left:295px; top:309px;">For Brothers &amp; Families</p>
    <p class="feature" style="left:179px; top:336px;">20 – 22 Days Trip</p>

    <svg class="divider bottom" viewBox="0 0 500 8" preserveAspectRatio="none" aria-hidden="true">
      <rect x="0" y="2" width="500" height="3" fill="url(#goldFade)"/>
    </svg>

    <div class="scene" role="img" aria-label="Illustration of the Kaaba between two white minarets and mosque arches"></div>

    <p class="with">With</p>
    <p class="guides">Sheikh Rehan Jameel Farooqui<br>&amp; Brother Bilal Qureshi</p>

    <svg class="footer-band" viewBox="0 0 500 106" preserveAspectRatio="none" aria-hidden="true">
      <defs>
        <linearGradient id="bandFill" x1="0" y1="0" x2="0" y2="1">
          <stop offset="0" stop-color="#5a4128"/>
          <stop offset="1" stop-color="#2e2013"/>
        </linearGradient>
      </defs>
      <path d="M0 12 Q250 50 500 6 L500 106 L0 106 Z" fill="url(#bandFill)"/>
      <path d="M0 12 Q250 50 500 6" fill="none" stroke="#f2c200" stroke-width="3"/>
    </svg>

    <p class="contact-name">Contact: Bilal Qureshi</p>

    <div class="contact-row phone">
      <svg class="contact-icon" viewBox="0 0 18 18" aria-hidden="true">
        <circle cx="9" cy="9" r="8" fill="none" stroke="#fff" stroke-width="1.3"/>
        <path d="M6 5.2c.4-.3.9-.2 1.1.2l.7 1.3c.2.4.1.8-.2 1l-.5.4c.4.9 1 1.5 1.9 1.9l.4-.5c.3-.3.7-.4 1-.2l1.3.7c.4.2.5.7.2 1.1l-.5.6c-.5.5-1.3.6-2 .3-1.9-.8-3.3-2.2-4.1-4.1-.3-.7-.2-1.5.3-2z" fill="#fff"/>
      </svg>
      <span>+92 333 5810462</span>
    </div>
    <div class="contact-row email">
      <svg class="contact-icon" viewBox="0 0 18 18" aria-hidden="true">
        <circle cx="9" cy="9" r="8" fill="none" stroke="#fff" stroke-width="1.3"/>
        <rect x="4.5" y="6" width="9" height="6.2" rx=".8" fill="none" stroke="#fff" stroke-width="1.1"/>
        <path d="M4.8 6.4 L9 9.6 L13.2 6.4" fill="none" stroke="#fff" stroke-width="1.1"/>
      </svg>
      <span>bilalqureshi@postmail.net</span>
    </div>
    <div class="contact-row web">
      <svg class="contact-icon" viewBox="0 0 18 18" aria-hidden="true">
        <circle cx="9" cy="9" r="8" fill="none" stroke="#fff" stroke-width="1.3"/>
      </svg>
      <span>youngpilgrims.net</span>
    </div>
  </main>
</body>
</html>
```